Design a Professional Stationery

Hi everyone,
I would like to make a design of stationery for my company Larvoni Wrap (www.larvoniwrap-example.com).
General Info: We are manufacturers of packaging supplies (poly bubble mailers, kraft bubble mailers, bubble wrap, tape, stretch film). We have couple of big warehouses in Los Angeles and New Jersey that serves East and West Coasts. We store lot of boxes with our product. We are wholesalers so we work with big serious distributors.

Project Goals: Create a business stationery that will look professional, modern and straight to the point. Colors: Dark blue, white, light blue (please see the web site). Blue is the color of success.
I want them to be presentable. As you might need to imagine my team will walk around the businesses and leave folders with information at clients table. We will distribute them at the trade shows, business meetings etc.

Target Market(s)

Business professionals looking for professional wholesaler manufacturer.

Industry/Entity Type

It Company

Font styles to use
Serif
Sans Serif

Colors
3276b5
0255a3
85acd3
cedeed
eaf1f7

Requirements
Must have
• People photos, product photos, add professional warehouse photos, truck, machinery.
Nice to have
• NLP
Should not have
• Use your imagination, no limits so far

```html
<!DOCTYPE html>
<html lang="en">
<head>
<meta charset="utf-8">
<title>Larvoni Wrap – Price List Sheet</title>
<link href="https://fonts.googleapis.com/css2?family=Lato:wght@400;700;900&display=swap" rel="stylesheet">
<style>
  :root {
    --navy: #1f3566;
    --blue: #3276b5;
    --rule: #9a9ea6;
    --row-fill: #ffffff;
    --ink: #2a2d33;
    --paper: #ffffff;
    --backdrop: #e9e9ea;
  }
  * { box-sizing: border-box; margin: 0; padding: 0; }
  html, body { width: 1200px; height: 1000px; overflow: hidden; }
  body {
    background: var(--backdrop);
    font-family: "Lato", Arial, sans-serif;
    color: var(--ink);
    position: relative;
  }
  .sheet {
    position: absolute;
    left: 267px; top: 24px;
    width: 666px; height: 952px;
    background: var(--paper);
  }
  .brand {
    position: absolute;
    left: 46px; top: 40px;
  }
  .brand-name {
    font-weight: 900;
    font-size: 27px;
    letter-spacing: 0.3px;
    color: var(--navy);
    text-transform: uppercase;
    line-height: 1;
    white-space: nowrap;
  }
  .brand-tagline {
    position: absolute;
    left: 46px; top: 82px;
    font-size: 7.6px;
    font-weight: 900;
    color: var(--navy);
    text-transform: uppercase;
    white-space: nowrap;
  }
  .contact {
    position: absolute;
    right: 42px; top: 40px;
    font-size: 9px;
    font-style: normal;
    color: var(--ink);
  }
  .contact-line { display: flex; gap: 10px; margin-bottom: 6px; }
  .contact-item {
    display: flex; align-items: center; gap: 5px;
    border-bottom: 1px solid var(--blue);
    padding-bottom: 1px;
    white-space: nowrap;
  }
  .contact-icon { width: 11px; height: 11px; flex: none; }
  .price-table {
    position: absolute;
    left: 46px; top: 126px;
    width: 576px;
    border-collapse: collapse;
    table-layout: fixed;
  }
  .price-table th {
    background: var(--navy);
    color: #fff;
    font-weight: 400;
    font-size: 11px;
    line-height: 1.15;
    height: 36px;
    border-left: 1px solid #fff;
    text-align: center;
  }
  .price-table th:first-child { border-left: none; }
  .price-table td {
    height: 30.3px;
    border: 1px solid var(--rule);
    background: var(--row-fill);
  }
  .validity {
    position: absolute;
    left: 0; top: 836px;
    width: 607px;
    font-size: 12.5px;
    font-weight: 700;
    font-style: italic;
    color: var(--ink);
  }
  .validity-row { display: flex; justify-content: flex-end; align-items: baseline; margin-bottom: 7px; }
  .validity-label { margin-right: 6px; }
  .validity-dots {
    width: 160px;
    border-bottom: 2px dotted #777;
    height: 10px;
  }
</style>
</head>
<body>
  <main class="sheet">
    <header>
      <div class="brand">
        <span class="brand-name">Larvoni Wrap</span>
      </div>
      <p class="brand-tagline">Manufacturer of poly and kraft bubble mailers</p>

      <address class="contact">
        <div class="contact-line">
          <span class="contact-item">
            <svg class="contact-icon" viewBox="0 0 12 12" aria-hidden="true"><rect width="12" height="12" fill="#3276b5"/><path d="M2.5 6.2 6 3l3.5 3.2V9.5h-2.2V7.3H4.7v2.2H2.5z" fill="#fff"/></svg>
            4200 Harlow Ave, Fernmoor CA 90210.
          </span>
        </div>
        <div class="contact-line">
          <span class="contact-item">
            <svg class="contact-icon" viewBox="0 0 12 12" aria-hidden="true"><rect width="12" height="12" fill="#3276b5"/><path d="M3.6 2.5l1.5 1.7-.8 1.1a5 5 0 0 0 2.4 2.4l1.1-.8 1.7 1.5-.8 1.1C6 9.5 2.5 6 2.5 3.3z" fill="#fff"/></svg>
            555-014-2290
          </span>
          <span class="contact-item">
            <svg class="contact-icon" viewBox="0 0 12 12" aria-hidden="true"><rect width="12" height="12" fill="#3276b5"/><circle cx="6" cy="6" r="3.3" fill="none" stroke="#fff" stroke-width="0.9"/><path d="M2.7 6h6.6M6 2.7c-1.4 1.8-1.4 4.8 0 6.6M6 2.7c1.4 1.8 1.4 4.8 0 6.6" fill="none" stroke="#fff" stroke-width="0.7"/></svg>
            www.larvoniwrap-example.com
          </span>
        </div>
      </address>
    </header>

    <table class="price-table">
      <colgroup>
        <col style="width:107px"><col style="width:76px"><col style="width:145px">
        <col style="width:83px"><col style="width:83px"><col style="width:82px">
      </colgroup>
      <thead>
        <tr>
          <th>Product Name</th>
          <th>Product Code</th>
          <th>Description</th>
          <th>Unit Price<br>(USD)</th>
          <th>Quantity</th>
          <th>Total Price<br>(USD)</th>
        </tr>
      </thead>
      <tbody>
        <tr><td></td><td></td><td></td><td></td><td></td><td></td></tr>
        <tr><td></td><td></td><td></td><td></td><td></td><td></td></tr>
        <tr><td></td><td></td><td></td><td></td><td></td><td></td></tr>
        <tr><td></td><td></td><td></td><td></td><td></td><td></td></tr>
        <tr><td></td><td></td><td></td><td></td><td></td><td></td></tr>
        <tr><td></td><td></td><td></td><td></td><td></td><td></td></tr>
        <tr><td></td><td></td><td></td><td></td><td></td><td></td></tr>
        <tr><td></td><td></td><td></td><td></td><td></td><td></td></tr>
        <tr><td></td><td></td><td></td><td></td><td></td><td></td></tr>
        <tr><td></td><td></td><td></td><td></td><td></td><td></td></tr>
        <tr><td></td><td></td><td></td><td></td><td></td><td></td></tr>
        <tr><td></td><td></td><td></td><td></td><td></td><td></td></tr>
        <tr><td></td><td></td><td></td><td></td><td></td><td></td></tr>
        <tr><td></td><td></td><td></td><td></td><td></td><td></td></tr>
        <tr><td></td><td></td><td></td><td></td><td></td><td></td></tr>
        <tr><td></td><td></td><td></td><td></td><td></td><td></td></tr>
        <tr><td></td><td></td><td></td><td></td><td></td><td></td></tr>
        <tr><td></td><td></td><td></td><td></td><td></td><td></td></tr>
        <tr><td></td><td></td><td></td><td></td><td></td><td></td></tr>
        <tr><td></td><td></td><td></td><td></td><td></td><td></td></tr>
        <tr><td></td><td></td><td></td><td></td><td></td><td></td></tr>
      </tbody>
    </table>

    <footer class="validity">
      <div class="validity-row"><span class="validity-label">Valid From:</span><span class="validity-dots"></span></div>
      <div class="validity-row"><span class="validity-label">To:</span><span class="validity-dots"></span></div>
    </footer>
  </main>
</body>
</html>
```